Packaging design for a low carb bar

I am producing a low carb / high fat bar, therefore I would like to have a light weighted modern design. The background color pastel light or something like that. The package should be focused on fitness-active individuals who are looking for healthy low carb snacks. Preliminary packaging size, logo, and more details on what should be attached to the packaging are attached. Thank you!

```html
<!DOCTYPE html>
<html lang="en">
<head>
<meta charset="utf-8">
<title>Keto Bar – Almond Flavour wrapper</title>
<link href="https://fonts.googleapis.com/css2?family=Amatic+SC:wght@400;700&family=Lato:wght@400;700&display=swap" rel="stylesheet">
<style>
  :root {
    --page: #f4f8f9;
    --teal: #2a8b93;
    --teal-deep: #1f7b83;
    --panel: #8fbfcc;
    --panel-soft: #a9cfd9;
    --wrap-white: #fbfcfc;
    --ink-teal: #3f8c98;
    --ring: #b7d6de;
    --ring-core: #5d9eab;
    --white: #ffffff;
  }
  * { box-sizing: border-box; margin: 0; padding: 0; }
  html, body { width: 1200px; height: 657px; overflow: hidden; background: var(--page); }
  .canvas { position: relative; width: 1200px; height: 657px; }
  .wrapper { position: absolute; left: 84px; top: 198px; width: 1056px; height: 304px; }
  .wrapper-shapes { position: absolute; inset: 0; }
  .flavour {
    position: absolute; left: 106px; top: 152px; width: 0; height: 0;
  }
  .flavour span {
    position: absolute; transform: translate(-50%, -50%) rotate(-90deg);
    font-family: "Lato", Arial, sans-serif; font-size: 19px; color: var(--white);
    white-space: nowrap; letter-spacing: 0.5px;
  }
  .product-name {
    position: absolute; left: 144px; top: 100px;
    font-family: "Amatic SC", "Comic Sans MS", cursive; font-weight: 700;
    font-size: 104px; line-height: 1; color: var(--white); letter-spacing: 1px;
  }
  .leaf-art {
    position: absolute; left: 398px; top: 188px; width: 60px; height: 58px;
    background: var(--panel-soft); border-radius: 4px;
  }
  .claims {
    position: absolute; left: 460px; top: 76px; transform: rotate(-8deg); transform-origin: left top;
    font-family: "Amatic SC", "Comic Sans MS", cursive; font-weight: 400; color: var(--ink-teal);
    list-style: none;
  }
  .claims li { position: relative; padding-left: 22px; line-height: 1; }
  .claims .bullet {
    position: absolute; left: 0; bottom: 6px; width: 14px; height: 12px;
    background: var(--ink-teal); border-radius: 2px;
  }
  .claim-keto { font-size: 34px; }
  .claim-keto .sub { display: block; font-size: 42px; padding-left: 14px; }
  .claim-carbs { font-size: 34px; margin-top: 8px; }
  .claim-carbs .big { font-size: 50px; }
  .claim-vegan { font-size: 50px; margin-top: 2px; }
  .brand {
    position: absolute; left: 708px; top: 58px; width: 204px; height: 204px;
    display: flex; align-items: center; justify-content: center;
  }
  .brand-circle {
    position: absolute; inset: 0; border-radius: 50%; background: var(--ring);
  }
  .brand-name {
    position: relative; font-family: "Amatic SC", "Comic Sans MS", cursive; font-weight: 400;
    font-size: 58px; color: var(--white); letter-spacing: 3px;
  }
  .ingredients {
    position: absolute; left: 960px; top: 152px; width: 0; height: 0;
  }
  .ingredients p {
    position: absolute; transform: translate(-50%, -50%) rotate(-90deg);
    font-family: "Lato", Arial, sans-serif; font-weight: 700; font-size: 9.5px; line-height: 1.5;
    color: var(--white); letter-spacing: 0.8px; text-transform: uppercase; width: 260px;
  }
</style>
</head>
<body>
<main class="canvas">
  <section class="wrapper" aria-label="Keto bar wrapper, almond flavour">
    <svg class="wrapper-shapes" width="1056" height="304" viewBox="0 0 1056 304" aria-hidden="true">
      <rect x="0" y="0" width="1056" height="304" fill="var(--wrap-white)"/>
      <rect class="end-seal-left" x="0" y="0" width="122" height="304" fill="var(--teal)"/>
      <rect class="flavour-stripe" x="90" y="0" width="32" height="304" fill="var(--teal-deep)"/>
      <path class="front-panel" d="M122 0 H510 C470 70 470 220 540 304 H122 Z" fill="var(--panel)"/>
      <rect class="end-seal-right" x="934" y="0" width="122" height="304" fill="var(--teal)"/>
      <rect class="ingredients-stripe" x="934" y="0" width="34" height="304" fill="var(--teal-deep)"/>
    </svg>
    <div class="flavour"><span>Almond Flavour</span></div>
    <h1 class="product-name">KETO BAR</h1>
    <div class="leaf-art" role="img" aria-label="Pair of white leaves"></div>
    <ul class="claims">
      <li class="claim-keto"><span class="bullet" role="img" aria-label="Small leaf"></span>Suitable for a keto<span class="sub">LCHF diet</span></li>
      <li class="claim-carbs"><span class="bullet" role="img" aria-label="Small leaf"></span>3.5g net <span class="big">carbs</span></li>
      <li class="claim-vegan"><span class="bullet" role="img" aria-label="Small leaf"></span>Vegan</li>
    </ul>
    <div class="brand">
      <span class="brand-circle"></span>
      <span class="brand-name">NORDLYN</span>
    </div>
    <div class="ingredients"><p>Peanuts, almonds, chia, coconut, sunflower and pumpkin seeds.</p></div>
  </section>
</main>
</body>
</html>
```